UI/ UX Design for ERP Software

We need a new UX/UI interface for a ERP software for property managers. Our CMMS / ERP solution is made based on responsive design technologies and is coded in PHP.
The overall UX to be similar to Zel Kavo - easy navigation, intuitive menus.

Industry/Entity Type

Property Management

Number of Pages Required

5+ page

Requirements
Must have
• Round dock buttons
Consistent icons across the application
Enough Spacing between buttons/icons/ menu
Consistent Font
Nice to have
• We would like the UX to allow the users to use the application without /minimum training.
Should not have
• we don't want anything that is classic with respect to UX

```html
<!DOCTYPE html>
<html lang="en">
<head>
<meta charset="utf-8">
<title>Domora — Dashboard</title>
<link href="https://fonts.googleapis.com/css2?family=IBM+Plex+Sans:wght@400;500;600&display=swap" rel="stylesheet">
<style>
:root{
  --brand:#0a7ff2;
  --brand-light:#00c2f7;
  --page:#e4f7fd;
  --white:#ffffff;
  --ink:#1a1a1a;
  --muted:#5a6470;
  --accent:#1677e6;
  --grid:#d8d8d8;
  --scheduled:#7eb0e8;
  --completed-sched:#8ced7a;
  --future:#f5a55f;
  --work-orders:#414148;
  --completed-wo:#8476ee;
  --inspect-progress:#e65c80;
  --inspect-done:#e0d556;
}
*{box-sizing:border-box;margin:0;padding:0}
html,body{width:1194px;height:1200px;overflow:hidden}
body{position:relative;background:var(--page);font-family:"IBM Plex Sans",sans-serif;color:var(--ink)}
.topbar{position:absolute;left:0;top:0;width:1194px;height:75px;background:linear-gradient(90deg,var(--brand),var(--brand-light))}
.brand{position:absolute;left:0;top:0;width:226px;height:75px;background:var(--brand);box-shadow:0 3px 6px rgba(0,0,0,.2);display:flex;align-items:center;justify-content:center;gap:8px;color:var(--white);font-weight:600;font-size:28px}
.brand .dot{width:14px;height:14px;border-radius:50%;background:var(--white)}
.search{position:absolute;left:548px;top:16px;width:387px;height:39px;background:#f4f4f4;border-radius:3px;font-size:13px;color:#888;padding:9px 16px}
.search svg{position:absolute;right:16px;top:12px}
.bell{position:absolute;left:985px;top:29px}
.avatar{border-radius:50%;background:linear-gradient(160deg,#c9a48a,#5a4a40);position:absolute}
.status{position:absolute;width:10px;height:10px;border-radius:50%;background:#1ee82e}
.top-user{position:absolute;left:1096px;top:28px;color:var(--white);font-size:14px;font-weight:500}
.sidebar{position:absolute;left:0;top:75px;width:225px;height:1125px;background:var(--white);box-shadow:2px 0 6px rgba(0,0,0,.06)}
.side-user{position:absolute;left:95px;top:118px;color:var(--accent);font-size:14px;font-weight:500}
.nav{position:absolute;left:0;top:169px;width:235px;list-style:none}
.nav li{height:41.8px;display:flex;align-items:center;padding-left:18px;gap:10px;color:var(--accent);font-size:12.8px;font-weight:500;position:relative;width:225px}
.nav li.active{height:53px;width:235px;background:linear-gradient(90deg,var(--brand),var(--brand-light));color:var(--white);margin-bottom:5px;box-shadow:0 3px 6px rgba(0,0,0,.15)}
.nav li svg{flex:none}
.nav .plus{position:absolute;left:203px;top:14px}
.stats{position:absolute;top:104px;left:0;width:1194px}
.stat{position:absolute;text-align:center;transform:translateX(-50%);white-space:nowrap}
.stat .label{font-size:13px;color:#555;font-weight:500}
.stat .value{font-size:18px;color:var(--brand-light);margin-top:2px;display:flex;align-items:center;justify-content:center;gap:6px}
.card{position:absolute;left:247px;top:177px;width:925px;height:569px;background:var(--white);border-radius:4px;box-shadow:0 2px 6px rgba(0,0,0,.12)}
.tabs{position:absolute;left:0;top:0;width:925px;height:62px;background:var(--brand-light);border-radius:4px 4px 0 0;box-shadow:0 3px 6px rgba(0,0,0,.12)}
.tab{position:absolute;top:11px;height:40px;line-height:40px;color:var(--white);font-size:12.8px;font-weight:600;display:flex;align-items:center;gap:4px}
.tab.active{background:var(--brand);border-radius:3px;padding:0 8px}
.range{position:absolute;left:28px;top:88px;color:var(--accent);font-size:13.5px;font-weight:500}
.chart{position:absolute;left:0;top:0}
.chart text{font-family:"IBM Plex Sans",sans-serif;font-size:9px;fill:#555}
.legend{position:absolute;width:290px;height:54px;background:var(--white);box-shadow:0 1px 4px rgba(0,0,0,.18);border-radius:2px;display:flex;align-items:center;gap:7px;padding-left:10px;font-size:14px;font-weight:500;color:#222}
.legend i{width:21px;height:21px;display:block}
.footer-line{position:absolute;left:225px;top:1139px;width:969px;height:1px;background:#888}
.footer-ver{position:absolute;left:1136px;top:1163px;font-size:10px;color:var(--accent)}
</style>
</head>
<body>
<header class="topbar">
  <div class="brand"><span class="dot"></span>Domora</div>
  <div class="search">Search
    <svg width="13" height="13" viewBox="0 0 13 13"><circle cx="5.5" cy="5.5" r="4" fill="none" stroke="#222" stroke-width="2"/><line x1="8.5" y1="8.5" x2="12" y2="12" stroke="#222" stroke-width="2"/></svg>
  </div>
  <svg class="bell" width="14" height="16" viewBox="0 0 14 16"><path d="M7 1a4 4 0 0 0-4 4v4l-2 3h12l-2-3V5a4 4 0 0 0-4-4z" fill="#fff"/><circle cx="7" cy="14" r="2" fill="#fff"/></svg>
  <div class="avatar" role="img" aria-label="User profile photo" style="left:1038px;top:13px;width:46px;height:46px"></div>
  <span class="status" style="left:1077px;top:15px"></span>
  <div class="top-user">ANNA REYES</div>
</header>

<aside class="sidebar">
  <div class="avatar" role="img" aria-label="User profile photo" style="left:37px;top:28px;width:46px;height:46px"></div>
  <span class="status" style="left:76px;top:31px"></span>
  <div class="side-user" style="top:43px">ANNA REYES</div>
  <ul class="nav" style="top:94px">
    <li class="active"><svg width="13" height="12" viewBox="0 0 13 12"><path d="M6.5 0L0 6h2v6h3.5V8h2v4H11V6h2z" fill="#fff"/></svg>Dashboard</li>
    <li><svg width="14" height="12" viewBox="0 0 14 12"><circle cx="7" cy="3" r="2.5" fill="currentColor"/><circle cx="2.5" cy="4" r="2" fill="currentColor"/><circle cx="11.5" cy="4" r="2" fill="currentColor"/><rect x="3" y="6.5" width="8" height="5" rx="2" fill="currentColor"/></svg>Customers</li>
    <li><svg width="13" height="12" viewBox="0 0 13 12"><path d="M6.5 0L0 6h2v6h3.5V8h2v4H11V6h2z" fill="currentColor"/></svg>Properties</li>
    <li><svg width="12" height="12" viewBox="0 0 12 12"><circle cx="6" cy="3" r="3" fill="currentColor"/><rect x="1" y="7" width="10" height="5" rx="2" fill="currentColor"/></svg>Tenants</li>
    <li><svg width="12" height="12" viewBox="0 0 12 12"><path d="M2 0l3 3-1.5 1.5a7 7 0 0 0 4 4L9 7l3 3-2 2C5 12 0 7 0 2z" fill="currentColor"/></svg>Contacts</li>
    <li><svg width="14" height="12" viewBox="0 0 14 12"><circle cx="5" cy="6" r="3.5" fill="none" stroke="currentColor" stroke-width="2.5"/><circle cx="11" cy="3" r="2" fill="currentColor"/><circle cx="11" cy="9" r="2" fill="currentColor"/></svg>Contractors</li>
    <li><svg width="14" height="12" viewBox="0 0 14 12"><circle cx="7" cy="3" r="2.5" fill="currentColor"/><circle cx="2.5" cy="4" r="2" fill="currentColor"/><circle cx="11.5" cy="4" r="2" fill="currentColor"/><rect x="3" y="6.5" width="8" height="5" rx="2" fill="currentColor"/></svg>Employees</li>
    <li><svg width="11" height="13" viewBox="0 0 11 13"><path d="M1 .5h6l3.5 3.5v8.5H1z" fill="none" stroke="currentColor"/></svg>Compliance Management</li>
    <li><svg width="14" height="12" viewBox="0 0 14 12"><circle cx="5" cy="6" r="3.5" fill="none" stroke="currentColor" stroke-width="2.5"/><circle cx="11" cy="3" r="2" fill="currentColor"/><circle cx="11" cy="9" r="2" fill="currentColor"/></svg>Prevent Maintenance<svg class="plus" width="11" height="11" viewBox="0 0 11 11"><rect x=".5" y=".5" width="10" height="10" rx="2" fill="none" stroke="currentColor"/><path d="M5.5 3v5M3 5.5h5" stroke="currentColor"/></svg></li>
    <li><svg width="12" height="12" viewBox="0 0 12 12"><circle cx="6" cy="6" r="4" fill="none" stroke="currentColor" stroke-width="3" stroke-dasharray="2.5 1"/></svg>Work Orders<svg class="plus" width="11" height="11" viewBox="0 0 11 11"><rect x=".5" y=".5" width="10" height="10" rx="2" fill="none" stroke="currentColor"/><path d="M5.5 3v5M3 5.5h5" stroke="currentColor"/></svg></li>
    <li><svg width="14" height="12" viewBox="0 0 14 12"><path d="M4 3L1 6l3 3M10 3l3 3-3 3M8 2L6 10" fill="none" stroke="currentColor" stroke-width="1.3"/></svg>Purchase Orders</li>
    <li><svg width="12" height="12" viewBox="0 0 12 12"><circle cx="5" cy="5" r="3.7" fill="none" stroke="currentColor" stroke-width="1.8"/><line x1="7.7" y1="7.7" x2="11" y2="11" stroke="currentColor" stroke-width="2"/></svg>Property Inspections<svg class="plus" width="11" height="11" viewBox="0 0 11 11"><rect x=".5" y=".5" width="10" height="10" rx="2" fill="none" stroke="currentColor"/><path d="M5.5 3v5M3 5.5h5" stroke="currentColor"/></svg></li>
    <li><svg width="14" height="12" viewBox="0 0 14 12"><path d="M1 0v11h13" fill="none" stroke="currentColor" stroke-width="1.3"/><rect x="3" y="5" width="2" height="5" fill="currentColor"/><rect x="6" y="3" width="2" height="7" fill="currentColor"/><rect x="9" y="6" width="2" height="4" fill="currentColor"/></svg>Energy Management</li>
    <li><svg width="13" height="12" viewBox="0 0 13 12"><path d="M6.5 0L13 12H0z" fill="currentColor"/><rect x="6" y="4" width="1" height="4" fill="#fff"/><rect x="6" y="9" width="1" height="1" fill="#fff"/></svg>Risk Management</li>
    <li><svg width="14" height="12" viewBox="0 0 14 12"><rect x=".5" y="1.5" width="13" height="9" fill="none" stroke="currentColor"/><path d="M3 4h8M3 6h8M3 8h8" stroke="currentColor"/></svg>Project Management</li>
    <li><svg width="14" height="12" viewBox="0 0 14 12"><rect x=".5" y="2.5" width="13" height="7" fill="none" stroke="currentColor"/><circle cx="7" cy="6" r="2" fill="currentColor"/></svg>Financial - Budgeting</li>
    <li><svg width="14" height="12" viewBox="0 0 14 12"><ellipse cx="6" cy="5" rx="5" ry="4" fill="none" stroke="currentColor" stroke-width="1.3"/><path d="M3 8l-1 3 4-2" fill="currentColor"/></svg>Tenant Requests</li>
    <li><svg width="11" height="13" viewBox="0 0 11 13"><path d="M1 .5h6l3.5 3.5v8.5H1z" fill="none" stroke="currentColor"/><path d="M3 6l4 4M7 6l-4 4" stroke="currentColor"/></svg>Reports<svg class="plus" width="11" height="11" viewBox="0 0 11 11"><rect x=".5" y=".5" width="10" height="10" rx="2" fill="none" stroke="currentColor"/><path d="M5.5 3v5M3 5.5h5" stroke="currentColor"/></svg></li>
    <li><svg width="14" height="12" viewBox="0 0 14 12"><path d="M1 0v11h13" fill="none" stroke="currentColor" stroke-width="1.3"/><rect x="3" y="5" width="2" height="5" fill="currentColor"/><rect x="6" y="3" width="2" height="7" fill="currentColor"/><rect x="9" y="6" width="2" height="4" fill="currentColor"/></svg>Visual Reports</li>
    <li><svg width="11" height="13" viewBox="0 0 11 13"><path d="M0 0h7l4 4v9H0z" fill="currentColor"/><path d="M2 7h7M2 9h7" stroke="#fff"/></svg>Files</li>
    <li><svg width="11" height="13" viewBox="0 0 11 13"><path d="M0 0h7l4 4v9H0z" fill="currentColor"/><path d="M2 7h7M2 9h7" stroke="#fff"/></svg>Pages<svg class="plus" width="11" height="11" viewBox="0 0 11 11"><rect x=".5" y=".5" width="10" height="10" rx="2" fill="none" stroke="currentColor"/><path d="M5.5 3v5M3 5.5h5" stroke="currentColor"/></svg></li>
    <li><svg width="14" height="12" viewBox="0 0 14 12"><circle cx="5" cy="6" r="3.5" fill="none" stroke="currentColor" stroke-width="2.5"/><circle cx="11" cy="3" r="2" fill="currentColor"/><circle cx="11" cy="9" r="2" fill="currentColor"/></svg>Configurations<svg class="plus" width="11" height="11" viewBox="0 0 11 11"><rect x=".5" y=".5" width="10" height="10" rx="2" fill="none" stroke="currentColor"/><path d="M5.5 3v5M3 5.5h5" stroke="currentColor"/></svg></li>
    <li><svg width="12" height="12" viewBox="0 0 12 12"><circle cx="6" cy="6" r="4" fill="none" stroke="currentColor" stroke-width="3" stroke-dasharray="2.5 1"/></svg>Settings<svg class="plus" width="11" height="11" viewBox="0 0 11 11"><rect x=".5" y=".5" width="10" height="10" rx="2" fill="none" stroke="currentColor"/><path d="M5.5 3v5M3 5.5h5" stroke="currentColor"/></svg></li>
  </ul>
</aside>

<section class="stats">
  <div class="stat" style="left:325px"><div class="label">PROPERTIES</div><div class="value"><svg width="16" height="14" viewBox="0 0 13 12"><path d="M6.5 0L0 6h2v6h3.5V8h2v4H11V6h2z" fill="currentColor"/></svg>3</div></div>
  <div class="stat" style="left:451px"><div class="label">TENANTS</div><div class="value"><svg width="18" height="15" viewBox="0 0 14 12"><circle cx="7" cy="3" r="2.5" fill="currentColor"/><circle cx="2.5" cy="4" r="2" fill="currentColor"/><circle cx="11.5" cy="4" r="2" fill="currentColor"/><rect x="3" y="6.5" width="8" height="5" rx="2" fill="currentColor"/></svg>8</div></div>
  <div class="stat" style="left:623px"><div class="label">TOTAL PROPERTIES AREA</div><div class="value"><svg width="16" height="16" viewBox="0 0 16 16"><path d="M8 0l3 3H9v4h4V5l3 3-3 3V9H9v4h2l-3 3-3-3h2V9H3v2L0 8l3-3v2h4V3H5z" fill="currentColor"/></svg>422,000.00 sq.ft.</div></div>
  <div class="stat" style="left:834px"><div class="label">RENTED AREA</div><div class="value"><svg width="16" height="16" viewBox="0 0 16 16"><path d="M8 0l3 3H9v4h4V5l3 3-3 3V9H9v4h2l-3 3-3-3h2V9H3v2L0 8l3-3v2h4V3H5z" fill="currentColor"/></svg>233,500.00 sq.ft.</div></div>
  <div class="stat" style="left:1042px"><div class="label">VACANCIES AREA</div><div class="value"><svg width="16" height="16" viewBox="0 0 16 16"><path d="M8 0l3 3H9v4h4V5l3 3-3 3V9H9v4h2l-3 3-3-3h2V9H3v2L0 8l3-3v2h4V3H5z" fill="currentColor"/></svg>188,500.00 sq.ft.</div></div>
</section>

<section class="card">
  <svg class="chart" width="925" height="569" viewBox="0 0 925 569">
    <g stroke="var(--grid)" stroke-width="1">
      <line x1="40" y1="140" x2="891" y2="140"/><line x1="40" y1="202.5" x2="891" y2="202.5"/>
      <line x1="40" y1="265" x2="891" y2="265"/><line x1="40" y1="327.5" x2="891" y2="327.5"/>
      <line x1="40" y1="390" x2="891" y2="390"/><line x1="40" y1="452.5" x2="891" y2="452.5"/>
      <line x1="40" y1="515" x2="891" y2="515"/><line x1="40" y1="140" x2="40" y2="515"/><line x1="891" y1="140" x2="891" y2="515"/>
    </g>
    <g text-anchor="end">
      <text x="33" y="143">1.5</text><text x="33" y="205">1.25</text><text x="33" y="268">1</text>
      <text x="33" y="330">0.75</text><text x="33" y="393">0.5</text><text x="33" y="455">0.25</text><text x="33" y="518">0</text>
    </g>
    <path d="M40,515 C90,470 130,444 171,444 C200,444 220,455 240,470 L380,455 C410,410 440,392 465,392 C495,392 520,410 545,440 L660,440 C690,405 715,388 745,388 C780,388 810,420 850,470 L891,480 L891,515 Z" fill="var(--scheduled)"/>
    <path d="M40,515 C120,500 190,480 240,420 C270,390 295,381 316,381 C350,381 370,415 400,450 C420,475 440,487 456,487 C490,487 510,450 530,410 C550,350 575,315 598,315 C625,315 650,340 686,420 C710,470 735,494 756,494 C780,494 800,470 827,450 L889,392 L891,515 Z" fill="var(--future)"/>
    <g fill="#1677e6"><circle cx="316" cy="381" r="2.5"/><circle cx="598" cy="315" r="2.5"/><circle cx="889" cy="392" r="2.5"/></g>
    <g fill="#19c6f0"><circle cx="139" cy="453" r="2.5"/><circle cx="465" cy="392" r="2.5"/><circle cx="721" cy="392" r="2.5"/></g>
    <g text-anchor="middle">
      <text x="92" y="537">27 Dec 2020</text><text x="199" y="537">28 Dec 2020</text><text x="307" y="537">29 Dec 2020</text>
      <text x="414" y="537">30 Dec 2020</text><text x="522" y="537">31 Dec 2020</text><text x="629" y="537">01 Jan 2021</text>
      <text x="736" y="537">02 Jan 2021</text><text x="844" y="537">03 Jan 2021</text>
    </g>
  </svg>
  <nav class="tabs">
    <span class="tab active" style="left:191px"><svg width="11" height="11" viewBox="0 0 11 11"><circle cx="5.5" cy="5.5" r="4.5" fill="none" stroke="#fff" stroke-width="1.5"/><path d="M5.5 3v3H3.5" fill="none" stroke="#fff" stroke-width="1.3"/></svg>Last 7 days</span>
    <span class="tab" style="left:311px"><svg width="11" height="11" viewBox="0 0 11 11"><circle cx="5.5" cy="5.5" r="4.5" fill="none" stroke="#fff" stroke-width="1.5"/><path d="M5.5 3v3H3.5" fill="none" stroke="#fff" stroke-width="1.3"/></svg>Last months</span>
    <span class="tab" style="left:432px"><svg width="11" height="11" viewBox="0 0 11 11"><circle cx="5.5" cy="5.5" r="4.5" fill="none" stroke="#fff" stroke-width="1.5"/><path d="M5.5 3v3H3.5" fill="none" stroke="#fff" stroke-width="1.3"/></svg> Last 3 months</span>
    <span class="tab" style="left:553px"><svg width="11" height="11" viewBox="0 0 11 11"><circle cx="5.5" cy="5.5" r="4.5" fill="none" stroke="#fff" stroke-width="1.5"/><path d="M5.5 3v3H3.5" fill="none" stroke="#fff" stroke-width="1.3"/></svg>Next 7 day</span>
    <span class="tab" style="left:674px"><svg width="11" height="11" viewBox="0 0 11 11"><circle cx="5.5" cy="5.5" r="4.5" fill="none" stroke="#fff" stroke-width="1.5"/><path d="M5.5 3v3H3.5" fill="none" stroke="#fff" stroke-width="1.3"/></svg>Next months</span>
    <span class="tab" style="left:796px"><svg width="11" height="11" viewBox="0 0 11 11"><circle cx="5.5" cy="5.5" r="4.5" fill="none" stroke="#fff" stroke-width="1.5"/><path d="M5.5 3v3H3.5" fill="none" stroke="#fff" stroke-width="1.3"/></svg> Next 3 months</span>
  </nav>
  <div class="range">12/27/2020 - 01/03/2021</div>
</section>

<div class="legend" style="left:250px;top:770px"><i style="background:var(--scheduled)"></i>Scheduled Maintenance</div>
<div class="legend" style="left:559px;top:770px"><i style="background:var(--completed-sched)"></i>Completed Scheduled Maintenance</div>
<div class="legend" style="left:868px;top:770px"><i style="background:var(--future)"></i>Future Scheduled Maintenance</div>
<div class="legend" style="left:250px;top:845px"><i style="background:var(--work-orders)"></i>Scheduled Work Orders</div>
<div class="legend" style="left:559px;top:845px"><i style="background:var(--completed-wo)"></i>Completed Work Orders</div>
<div class="legend" style="left:868px;top:845px"><i style="background:var(--inspect-progress)"></i>Property Inspections in Progress</div>
<div class="legend" style="left:250px;top:919px"><i style="background:var(--inspect-done)"></i>Completed Property Inspections</div>

<div class="footer-line"></div>
<div class="footer-ver">C 43</div>
</body>
</html>
```